Super elegant, crisp & clean Business card design required

We recently upgraded our branding - which is on our website - tavolenstudio.com

I would like a simple, yet elegant, clean business card design please.

The font of my logo is Cinzel - and because of the natural colour - it's best to have this on a black background.

I would like to have the back of the business card - with simply my logo.

PLEASE DO NOT SUBMIT A COMPLICATED / UNCLEAN DESIGN

Industry/Entity Type

Business

Contact Information for Business Card

Danvir Okelowa Photography

Font styles to use
Other font styles liked:
• Cinzel

Requirements
Must have
• A backpage with nothing but my logo
• Simple design - stands out
Should not have
• Colour that dont align with my logo
• Over complicated '/ non symmetrical design

```html
<!DOCTYPE html>
<html lang="en">
<head>
<meta charset="utf-8">
<title>Danvir Okelowa Photography – Business Card</title>
<link rel="stylesheet" href="https://fonts.googleapis.com/css2?family=Cinzel:wght@400;500&family=Arimo:wght@400&display=swap">
<style>
  :root {
    --stage: #e9e6e0;
    --paper: #fbfbf9;
    --band-dark: #57524a;
    --band-taupe: #9c9380;
    --tab: #6d665a;
    --gold: #a89c82;
    --ink-light: #ffffff;
    --rule: rgba(255,255,255,0.55);
  }
  * { box-sizing: border-box; margin: 0; padding: 0; }
  html, body { width: 1200px; height: 902px; overflow: hidden; }
  body { background: var(--stage); position: relative; font-family: "Arimo", sans-serif; }

  .card {
    position: absolute;
    width: 560px; height: 320px;
    background: var(--paper);
    box-shadow: 0 10px 28px rgba(0,0,0,0.18);
    overflow: hidden;
  }
  .card--front { left: 70px; top: 90px; }
  .card--back  { left: 570px; top: 490px; }

  .card__top-band {
    position: absolute; left: 0; top: 0; width: 100%; height: 38px;
    background: var(--band-dark);
  }
  .card__lower-band { position: absolute; left: 0; top: 170px; width: 560px; height: 150px; }

  .wordmark {
    position: absolute; left: 0; width: 100%;
    text-align: center; color: var(--gold);
    font-family: "Cinzel", serif; font-weight: 400;
  }
  .card--front .wordmark { top: 82px; }
  .card--back  .wordmark { top: 118px; }
  .wordmark__name { display: block; letter-spacing: 0.5px; }
  .wordmark__trade { display: block; letter-spacing: 9px; }
  .card--front .wordmark__name  { font-size: 25px; }
  .card--front .wordmark__trade { font-size: 11px; margin-top: 2px; }
  .card--back  .wordmark__name  { font-size: 34px; }
  .card--back  .wordmark__trade { font-size: 14px; margin-top: 4px; letter-spacing: 12px; }

  .owner {
    position: absolute; left: 128px; top: 178px;
    display: flex; align-items: center; gap: 8px;
    color: var(--ink-light);
  }
  .owner__name { font-family: "Cinzel", serif; font-size: 15px; letter-spacing: 0.5px; line-height: 1.1; }
  .owner__role { font-family: "Cinzel", serif; font-size: 10px; letter-spacing: 1px; }

  .contacts {
    position: absolute; left: 0; bottom: 26px; width: 100%;
    display: flex; justify-content: center; align-items: flex-end;
    color: var(--ink-light); font-size: 13px; letter-spacing: 0.3px;
  }
  .contacts__item {
    display: flex; flex-direction: column; align-items: center; gap: 8px;
    padding: 0 14px;
  }
  .contacts__item + .contacts__item { border-left: 1px solid var(--rule); }
  .contacts__icon { width: 18px; height: 18px; }
</style>
</head>
<body>

<section class="card card--front" aria-label="Business card front">
  <div class="card__top-band"></div>

  <svg class="card__lower-band" viewBox="0 0 560 150" aria-hidden="true">
    <polygon points="0,40 150,40 150,0 560,0 560,150 0,150" fill="var(--band-taupe)"/>
    <polygon points="112,8 315,8 330,22 315,70 125,70 112,56" fill="var(--tab)"/>
  </svg>

  <div class="wordmark">
    <span class="wordmark__name">Danvir Okelowa</span>
    <span class="wordmark__trade">Photography</span>
  </div>

  <div class="owner">
    <svg class="contacts__icon" viewBox="0 0 18 18" aria-hidden="true">
      <circle cx="9" cy="9" r="9" fill="#fff"/>
      <circle cx="9" cy="7" r="3" fill="var(--tab)"/>
      <path d="M3.5 15 a5.5 5 0 0 1 11 0z" fill="var(--tab)"/>
    </svg>
    <div>
      <div class="owner__name">Danvir Okelowa</div>
      <div class="owner__role">Owner</div>
    </div>
  </div>

  <div class="contacts">
    <div class="contacts__item">
      <svg class="contacts__icon" viewBox="0 0 18 18" aria-hidden="true">
        <path d="M9 2 L16 8 V16 H2 V8z" fill="#fff"/>
        <text x="9" y="14" font-size="7" text-anchor="middle" fill="var(--band-taupe)" font-family="Arimo, sans-serif">@</text>
      </svg>
      <span>www.tavolenstudio.com</span>
    </div>
    <div class="contacts__item">
      <svg class="contacts__icon" viewBox="0 0 18 18" aria-hidden="true">
        <circle cx="9" cy="9" r="9" fill="#fff"/>
        <path d="M5.5 5 l2 -0.5 l1 2.5 l-1.2 1 a6 6 0 0 0 2.7 2.7 l1 -1.2 l2.5 1 l-0.5 2 c-4 0.5 -8 -3.5 -7.5 -7.5z" fill="var(--band-taupe)"/>
      </svg>
      <span>07946128305</span>
    </div>
    <div class="contacts__item">
      <svg class="contacts__icon" viewBox="0 0 18 18" aria-hidden="true">
        <circle cx="9" cy="9" r="9" fill="#fff"/>
        <rect x="4" y="5.5" width="10" height="7" fill="var(--band-taupe)"/>
        <path d="M4 5.5 L9 9.5 L14 5.5" stroke="#fff" stroke-width="1" fill="none"/>
      </svg>
      <span>info@tavolenstudio.com</span>
    </div>
  </div>
</section>

<section class="card card--back" aria-label="Business card back">
  <div class="wordmark">
    <span class="wordmark__name">Danvir Okelowa</span>
    <span class="wordmark__trade">Photography</span>
  </div>
</section>

</body>
</html>
```